Redesign of Leavely Calendar website

Looking to drastically improve our Leavely (paid time off) Calendar look and feel. Need a modern and well thought out design that is fun.
Current Screenshots
https://files.brindlemoor.net/sheet/p/7vTq2LmW9xZpK4nRb8JsYcHa3eDfG5uNwQ1tVhXo/view?mode=public
It's written in PHP and Laravel, if that matters. I am not necessarily attached to any of the current design, so please go wild. Current functionality needs to remain the same, but some can be added if you feel it would be of value. Layout can certainly change.
NOTE - this calendar can be used by any company, not just our own. So we'd like it to have a look and feel that is easy to navigate.
Site logo is attached.
Pages needed:
* Login Page
* Registration Page
* Calendar page
* Add Leavely method
* Admin page (will use template for all admin areas)
* User profile page
Thanks!

```html
<!DOCTYPE html>
<html lang="en">
<head>
<meta charset="utf-8">
<title>Leavely — Login</title>
<link href="https://fonts.googleapis.com/css2?family=Montserrat:wght@400;500;600;700&display=swap" rel="stylesheet">
<style>
  :root{
    --ink:#3a4756;
    --blue:#0673c4;
    --blue-dark:#0561a8;
    --blue-light:#1287d6;
    --muted:#9aa4ae;
    --line:#d9dee3;
    --page-alt:#e9eef3;
    --sq-light:#c9e0f0;
    --sq-grey:#c5c9ce;
    --white:#ffffff;
  }
  *{box-sizing:border-box;margin:0;padding:0}
  html,body{width:1030px;height:1200px;overflow:hidden}
  body{font-family:'Montserrat',sans-serif;color:var(--ink);background:var(--white);position:relative}
  .variant{position:absolute;left:0;width:1030px}
  .variant--light{top:0;height:603px;background:var(--white)}
  .variant--soft{top:603px;height:597px;background:var(--page-alt)}
  .brand{position:absolute;left:0;width:1030px;top:44px;display:flex;justify-content:center;align-items:center;gap:6px;
    font-weight:700;font-size:30px;letter-spacing:-0.5px;color:var(--ink)}
  .brand__dot{width:22px;height:22px;border-radius:50%;background:var(--blue)}
  .deco{position:absolute}
  .deco--light{left:246px;top:95px;width:26px;height:26px;background:var(--sq-light)}
  .deco--grey{left:266px;top:127px;width:17px;height:17px;background:var(--sq-grey)}
  .deco--blue{left:215px;top:130px;width:42px;height:42px;background:var(--blue);border-radius:3px;
    box-shadow:0 10px 20px rgba(6,115,196,.25);z-index:2}
  .card{position:absolute;left:235px;top:105px;width:562px;height:379px;background:var(--white);
    border-radius:19px;overflow:hidden;box-shadow:0 20px 50px rgba(40,70,100,.12)}
  .card__art{position:absolute;left:0;top:0}
  .login__title{position:absolute;left:61px;top:54px;font-size:30px;font-weight:700;color:var(--ink)}
  .login__rule{position:absolute;left:62px;top:101px;width:20px;height:2px;background:var(--blue)}
  .field__label{position:absolute;left:62px;top:137px;font-size:6.5px;font-weight:600;letter-spacing:1px;color:var(--blue)}
  .field{position:absolute;left:62px;width:208px;height:14px;display:flex;align-items:center;gap:5px;font-size:8px}
  .field--user{top:153px;color:var(--ink);font-weight:500}
  .field--pass{top:192px;color:var(--muted)}
  .field__eye{margin-left:auto}
  .field__line{position:absolute;left:62px;width:208px;height:1px;background:var(--line)}
  .field__line--active{top:171px;background:var(--blue)}
  .field__line--pass{top:212px}
  .options{position:absolute;left:62px;top:226px;width:208px;display:flex;align-items:center;font-size:5.5px}
  .options__check{width:9px;height:9px;border:1px solid var(--sq-grey);border-radius:2px;margin-right:6px}
  .options__remember{color:var(--muted)}
  .options__forgot{margin-left:auto;margin-right:6px;color:var(--blue);font-weight:600}
  .btn-login{position:absolute;left:62px;top:261px;width:208px;height:26px;border-radius:3px;
    background:linear-gradient(90deg,var(--blue-dark),var(--blue-light),var(--blue-dark));color:var(--white);
    font-size:7.5px;font-weight:600;display:flex;align-items:center;justify-content:center;
    box-shadow:0 10px 18px rgba(6,115,196,.2)}
  .register{position:absolute;left:62px;width:208px;top:309px;text-align:center;font-size:7.5px;color:var(--muted)}
  .register a{color:var(--blue);text-decoration:none}
  .copyright{position:absolute;left:0;width:1030px;top:526px;text-align:center;font-size:8px;color:var(--ink)}
</style>
</head>
<body>

<section class="variant variant--light">
  <div class="brand"><span>Leavely</span><span class="brand__dot"></span></div>
  <span class="deco deco--light"></span><span class="deco deco--grey"></span><span class="deco deco--blue"></span>
  <div class="card">
    <svg class="card__art" width="562" height="379" viewBox="0 0 562 379">
      <defs>
        <linearGradient id="blobBlue" x1="0" y1="0" x2="1" y2="1">
          <stop offset="0" stop-color="#0589d2"/><stop offset="1" stop-color="#0565b9"/>
        </linearGradient>
      </defs>
      <path d="M562 0 L520 0 C380 6 290 90 290 195 C290 300 380 372 460 379 L562 379 Z" fill="url(#blobBlue)"/>
      <rect x="359" y="78" width="203" height="228" rx="6" fill="#1f8fd6" opacity=".55" role="img" aria-label="Illustration of a person standing beside a large phone showing a login screen"/>
    </svg>
    <div class="login__title">Login</div><span class="login__rule"></span>
    <div class="field__label">USERNAME</div>
    <div class="field field--user">
      <svg width="9" height="9" viewBox="0 0 10 10"><circle cx="5" cy="3" r="2.2" fill="none" stroke="#3a4756"/><path d="M1 9.5 C1 6.5 9 6.5 9 9.5 Z" fill="none" stroke="#3a4756"/></svg>JHON DOE</div>
    <span class="field__line field__line--active"></span>
    <div class="field field--pass">
      <svg width="9" height="9" viewBox="0 0 10 10"><rect x="1" y="4.5" width="8" height="5" rx="1" fill="none" stroke="#b5bcc3"/><path d="M3 4.5 V3 a2 2 0 0 1 4 0 V4.5" fill="none" stroke="#b5bcc3"/></svg>PASSWORD
      <svg class="field__eye" width="10" height="7" viewBox="0 0 10 7"><path d="M0.5 3.5 C3 0 7 0 9.5 3.5 C7 7 3 7 0.5 3.5Z" fill="none" stroke="#b5bcc3"/><circle cx="5" cy="3.5" r="1.3" fill="#b5bcc3"/></svg></div>
    <span class="field__line field__line--pass"></span>
    <div class="options"><span class="options__check"></span><span class="options__remember">REMEMBER ME</span><span class="options__forgot">FORGOT PASSWORD?</span></div>
    <div class="btn-login">LOGIN</div>
    <div class="register">Don't have an account yet? <a href="#">Register here</a></div>
  </div>
  <div class="copyright">Copyright © 2020. All Rights Reserved to Leavely.</div>
</section>

<section class="variant variant--soft">
  <div class="brand" style="top:60px"><span>Leavely</span><span class="brand__dot"></span></div>
  <span class="deco deco--light" style="top:107px"></span><span class="deco deco--grey" style="top:139px"></span><span class="deco deco--blue" style="top:142px"></span>
  <div class="card" style="top:118px">
    <svg class="card__art" width="562" height="379" viewBox="0 0 562 379">
      <defs>
        <linearGradient id="softArt" x1="0" y1="0" x2="1" y2="1">
          <stop offset="0" stop-color="#eef2f5"/><stop offset=".55" stop-color="#cfe2f2"/><stop offset="1" stop-color="#eef2f5"/>
        </linearGradient>
      </defs>
      <rect x="306" y="55" width="256" height="277" rx="6" fill="url(#softArt)" role="img" aria-label="Illustration of a person beside a large blue phone showing a login screen, in a light room"/>
    </svg>
    <div class="login__title">Login</div><span class="login__rule"></span>
    <div class="field__label">USERNAME</div>
    <div class="field field--user">
      <svg width="9" height="9" viewBox="0 0 10 10"><circle cx="5" cy="3" r="2.2" fill="none" stroke="#3a4756"/><path d="M1 9.5 C1 6.5 9 6.5 9 9.5 Z" fill="none" stroke="#3a4756"/></svg>JHON DOE</div>
    <span class="field__line field__line--active"></span>
    <div class="field field--pass">
      <svg width="9" height="9" viewBox="0 0 10 10"><rect x="1" y="4.5" width="8" height="5" rx="1" fill="none" stroke="#b5bcc3"/><path d="M3 4.5 V3 a2 2 0 0 1 4 0 V4.5" fill="none" stroke="#b5bcc3"/></svg>PASSWORD
      <svg class="field__eye" width="10" height="7" viewBox="0 0 10 7"><path d="M0.5 3.5 C3 0 7 0 9.5 3.5 C7 7 3 7 0.5 3.5Z" fill="none" stroke="#b5bcc3"/><circle cx="5" cy="3.5" r="1.3" fill="#b5bcc3"/></svg></div>
    <span class="field__line field__line--pass"></span>
    <div class="options"><span class="options__check"></span><span class="options__remember">REMEMBER ME</span><span class="options__forgot">FORGOT PASSWORD?</span></div>
    <div class="btn-login">LOGIN</div>
    <div class="register">Don't have an account yet? <a href="#">Register here</a></div>
  </div>
  <div class="copyright" style="top:539px">Copyright © 2020. All Rights Reserved to Leavely.</div>
</section>

</body>
</html>
```